Parcel Meadow
Website design - Gifts and Occasions
Website design
Gifts and Occasions
The company is a gift giving service that helps people pick out the perfect gift based on an algorthim
above header
https://www.chatterloop.com/
BrightMarble BrightMarble
please extend this contest

```html
<!DOCTYPE html>
<html lang="en">
<head>
<meta charset="utf-8">
<title>Parcel Meadow</title>
<link href="https://fonts.googleapis.com/css2?family=Signika:wght@300;400&family=Arimo:wght@400&display=swap" rel="stylesheet">
<style>
:root{
  --band:#60b9c3;
  --hero:#a3dde1;
  --ring:#9fd9de;
  --brown:#7a5200;
  --heading:#7a5300;
  --text:#2a2a2a;
  --muted:#8a8a8a;
  --field-border:#e2e2e2;
  --page:#f8f8f8;
  --white:#ffffff;
  --teal-text:#4fb3bd;
  --arrow:#8a7cc4;
}
*{box-sizing:border-box;margin:0;padding:0}
html,body{width:1200px;height:956px;overflow:hidden}
body{background:var(--page);font-family:"Signika",sans-serif;font-weight:300;color:var(--text);position:relative}
h2{font-weight:300}
.top-band{position:absolute;left:0;top:0;width:1200px;height:66px;background:var(--band)}
.hero{position:absolute;left:0;top:66px;width:1200px;height:272px;background:var(--hero)}
.brand-disc{position:absolute;left:80px;top:17px;width:304px;height:304px;border-radius:50%;background:var(--white);display:flex;align-items:center;justify-content:center}
.brand-disc::after{content:"";position:absolute;inset:9px;border-radius:50%;border:3px solid var(--ring)}
.brand-name{font-size:30px;font-weight:300;color:var(--brown);letter-spacing:1px;white-space:nowrap}
.tagline{position:absolute;left:420px;top:118px;width:330px;font-size:23px;line-height:32px;color:var(--white)}
.login-title{position:absolute;left:790px;top:16px;font-size:23px;font-weight:300;color:var(--white);white-space:nowrap}
.login{position:absolute;left:792px;top:94px;width:328px}
.login .field{height:37px;background:var(--white);margin-bottom:10px;padding-left:15px;font-size:17px;line-height:37px;color:var(--teal-text)}
.remember{display:flex;align-items:center;gap:6px;font-size:15px;color:var(--white);margin-top:4px;white-space:nowrap}
.tick-box{width:16px;height:16px;background:var(--white);display:flex;align-items:center;justify-content:center}
.btn{display:inline-block;background:var(--brown);color:var(--white);font-size:18px;height:37px;line-height:37px;padding:0 15px;font-weight:300;white-space:nowrap;text-align:center;min-width:89px}
.login .btn{margin-top:14px}
.forgot{margin-top:12px;font-size:15px;color:var(--white);white-space:nowrap}
.section-title{font-size:23px;color:var(--heading);font-weight:300;white-space:nowrap}
.about{position:absolute;left:79px;top:362px;width:627px}
.about p{font-size:15.5px;line-height:23px;margin-left:1px;margin-top:10px;text-align:justify}
.about p + p{margin-top:22px}
.how{position:absolute;left:78px;top:556px}
.step{position:absolute;top:44px;width:140px;text-align:center}
.step-art{width:140px;height:140px;border-radius:50%;border:5px solid var(--ring);background:radial-gradient(circle at 50% 55%,#f1d3b0 0%,#c6e6ea 55%,#ffffff 80%)}
.step-label{margin-top:12px;font-size:19px;line-height:24px;color:var(--text)}
.step-arrow{position:absolute;top:108px}
.signup{position:absolute;left:790px;top:362px;width:330px}
.signup .field{position:relative;height:38px;margin-left:2px;width:328px;background:var(--white);border:1px solid var(--field-border);margin-top:9px;padding-left:14px;font-size:16px;line-height:36px;color:var(--muted);white-space:nowrap}
.signup .section-title{margin-bottom:11px}
.gender{display:flex;align-items:center;margin:15px 0 12px 2px;font-size:16px;color:var(--text);height:28px;white-space:nowrap}
.gender .label{width:89px;color:#555}
.radio{width:26px;height:26px;border-radius:50%;border:1px solid var(--field-border);background:var(--white);display:flex;align-items:center;justify-content:center;margin-right:10px}
.radio.on::after{content:"";width:12px;height:12px;border-radius:50%;background:#e2e2e2}
.gender .opt{margin-right:24px}
.field-icon{position:absolute;right:10px;top:8px}
.signup .btn{margin-top:19px;margin-left:2px}
.footer{position:absolute;left:0;top:918px;width:1200px;border-top:1px solid #e6e6e6;height:38px;font-family:"Arimo",sans-serif;font-size:11.5px;color:#555;white-space:nowrap}
.footer nav{position:absolute;left:80px;top:12px;display:flex;gap:17px}
.footer .legal{position:absolute;right:80px;top:12px}
</style>
</head>
<body>
  <div class="top-band"></div>
  <div class="hero" role="img" aria-label="Soft teal backdrop with a faint pattern of outlined gift boxes"></div>

  <div class="brand-disc"><span class="brand-name">Parcel Meadow</span></div>
  <p class="tagline">A gift giving service that helps people pick out the perfect gift based on an algorthim</p>

  <h2 class="login-title">Sign In</h2>
  <form class="login">
    <div class="field">Username</div>
    <div class="field">Password</div>
    <div class="remember"><span class="tick-box"><svg width="12" height="10" viewBox="0 0 12 10"><path d="M1 5l3.5 3.5L11 1.5" fill="none" stroke="#4fb3bd" stroke-width="2"/></svg></span>Keep me logged in</div>
    <span class="btn">Login</span>
    <p class="forgot">Forgot your password?</p>
  </form>

  <section class="about">
    <h2 class="section-title">About Us</h2>
    <p>Parcel Meadow is a gift giving service that recommends the best gift for your personal or professional relationship. We will organize your upcoming events and notify you if a gift may need to be sent.</p>
    <p>Parcel Meadow utilizes complex computer algorithms to recommend you a gift.</p>
  </section>

  <section class="how">
    <h2 class="section-title">How It Works?</h2>
    <div class="step" style="left:2px">
      <div class="step-art" role="img" aria-label="Illustration of a wrapped gift box with a red ribbon"></div>
      <p class="step-label">Find a Gift</p>
    </div>
    <svg class="step-arrow" style="left:148px" width="62" height="16" viewBox="0 0 62 16"><path d="M2 9 Q30 6 58 8 M50 2 L58 8 L50 14" fill="none" stroke="var(--arrow)" stroke-width="1.2"/></svg>
    <div class="step" style="left:218px">
      <div class="step-art" role="img" aria-label="Illustration of hands filling out a form on a tablet"></div>
      <p class="step-label">Fill out the basic information</p>
    </div>
    <svg class="step-arrow" style="left:364px" width="62" height="16" viewBox="0 0 62 16"><path d="M2 9 Q30 6 58 8 M50 2 L58 8 L50 14" fill="none" stroke="var(--arrow)" stroke-width="1.2"/></svg>
    <div class="step" style="left:433px">
      <div class="step-art" role="img" aria-label="Illustration of a finger selecting a contact on a tablet"></div>
      <p class="step-label">Select Contact</p>
    </div>
  </section>

  <form class="signup">
    <h2 class="section-title">Sign In</h2>
    <div class="field">First Name</div>
    <div class="field">Last Name</div>
    <div class="field">Email</div>
    <div class="field">Username</div>
    <div class="field">Password</div>
    <div class="field">Re-Enter Password<svg class="field-icon" style="top:14px" width="16" height="9" viewBox="0 0 16 9"><path d="M0 0h16L8 9z" fill="#b5b5b5"/></svg></div>
    <div class="field">Security Question</div>
    <div class="gender">
      <span class="label">Gender</span>
      <span class="radio on"></span><span class="opt">Male</span>
      <span class="radio"></span><span>Female</span>
    </div>
    <div class="field" style="margin-top:0">Birthday<svg class="field-icon" style="top:6px" width="22" height="23" viewBox="0 0 22 23"><rect x="1" y="3" width="20" height="19" fill="none" stroke="#c4c4c4" stroke-width="2"/><rect x="1" y="3" width="20" height="4" fill="#c4c4c4"/><rect x="5" y="0" width="2" height="5" fill="#c4c4c4"/><rect x="15" y="0" width="2" height="5" fill="#c4c4c4"/><g fill="#c4c4c4"><rect x="5" y="10" width="3" height="3"/><rect x="10" y="10" width="3" height="3"/><rect x="15" y="10" width="3" height="3"/><rect x="5" y="15" width="3" height="3"/><rect x="10" y="15" width="3" height="3"/><rect x="15" y="15" width="3" height="3"/></g></svg></div>
    <span class="btn">Sign Up</span>
  </form>

  <footer class="footer">
    <nav>
      <span>About</span><span>Buy a gift</span><span>Upcoming Events</span><span>FeedBack</span><span>NewsFeed</span><span>What's Trending</span><span>Developers</span><span>Careers</span><span>Privacy</span><span>Cookies</span><span>Terms</span><span>Help</span>
    </nav>
    <span class="legal">© 2014. All Rights Reserved</span>
  </footer>
</body>
</html>
```